Olive Oil Label Needs Graphic Designs

We need two sister label designs for 500ml bottles for our new brand "Casa Lumbre". Casa Lumbre is a high-end olive oil from Baeza, Spain which will be sold in the US. The oil will be produced from both Arbequina olives and Picual olives. Therefore, envisioning the same design just a different color scheme for the different labels.
The label should have the following characteristics; clean and simple, stand-out from mainstream labels, be eye-catching, give perception of high-end / high-quality.
Our current thinking of what we want (but please let your creative juices flow); lighter background, to be more eye catching, graphics of and olive, a olive branch or olive tree.
Text which should appear on the label are (not necessarily in this order);
Casa Lumbre
Extra Virgin Olive Oil
Family Reserve
Arbequina (One design)
Picual (Second design)
The label should be about 3 inches wide and 5.5 inches in height.

```html
<!DOCTYPE html>
<html lang="en">
<head>
<meta charset="utf-8">
<title>Casa Lumbre Picual – Extra Virgin Olive Oil Label</title>
<link rel="stylesheet" href="https://fonts.googleapis.com/css2?family=Almendra+Display&family=Oranienbaum&family=Cinzel:wght@700&family=Sofia&display=swap">
<style>
  :root {
    --page: #ffffff;
    --label-red: #7a1218;
    --band-red: #5c1a22;
    --frame-maroon: #5e1d2a;
    --gold-edge: #8a7636;
    --cream: #f3e797;
    --cream-line: #efe2b0;
    --text-cream: #f8f1d8;
    --olive-green: #7c8a4a;
    --picual-maroon: #6a1a2a;
    --rule-dark: #1e1a16;
  }
  html, body {
    margin: 0;
    padding: 0;
    width: 800px;
    height: 1200px;
    overflow: hidden;
    background: var(--page);
  }
  .label-canvas {
    display: block;
    width: 800px;
    height: 1200px;
  }
  .label-body { fill: var(--label-red); stroke: var(--gold-edge); stroke-width: 6; }
  .top-band { fill: var(--band-red); }
  .band-rule { stroke: var(--gold-edge); stroke-width: 2; }
  .frame-outer { fill: var(--frame-maroon); stroke: var(--cream-line); stroke-width: 2; }
  .frame-mid { fill: none; stroke: var(--cream-line); stroke-width: 3; }
  .frame-inner { fill: var(--cream); stroke: var(--frame-maroon); stroke-width: 5; }
  .rule { stroke: var(--rule-dark); }
  .tree-art { fill: var(--olive-green); }
  .branch-art { fill: #9aa35e; }
  .reserve-title {
    font-family: "Almendra Display", serif;
    font-size: 62px;
    fill: var(--text-cream);
    letter-spacing: 1px;
  }
  .brand-name {
    font-family: "Sofia", cursive;
    font-size: 104px;
    fill: var(--olive-green);
  }
  .variety-name {
    font-family: "Sofia", cursive;
    font-size: 104px;
    fill: var(--picual-maroon);
  }
  .product-type {
    font-family: "Oranienbaum", serif;
    font-size: 66px;
    fill: var(--text-cream);
  }
  .volume {
    font-family: "Cinzel", serif;
    font-weight: 700;
    font-size: 50px;
    fill: var(--text-cream);
  }
  .volume-unit { font-size: 36px; }
</style>
</head>
<body>
<svg class="label-canvas" viewBox="0 0 800 1200" xmlns="http://www.w3.org/2000/svg">
  <defs>
    <clipPath id="label-shape">
      <rect x="28" y="45" width="754" height="1037" rx="140" ry="150"/>
    </clipPath>
    <path id="badge-shape" d="M405,190 Q520,222 655,222 L655,258 L700,258 L700,300 Q725,300 725,330 L755,330 L755,770 L725,770 Q725,800 700,800 L700,842 L655,842 Q520,842 405,860 Q290,842 155,842 L110,842 L110,800 Q85,800 85,770 L55,770 L55,330 L85,330 Q85,300 110,300 L110,258 L155,258 L155,222 Q290,222 405,190 Z"/>
  </defs>

  <g class="label">
    <rect class="label-body" x="28" y="45" width="754" height="1037" rx="140" ry="150"/>
    <rect class="top-band" x="28" y="45" width="754" height="117" clip-path="url(#label-shape)"/>
    <line class="band-rule" x1="60" y1="162" x2="750" y2="162"/>
    <rect x="28" y="45" width="754" height="1037" rx="140" ry="150" fill="none" stroke="#8a7636" stroke-width="6"/>

    <text class="reserve-title" x="405" y="135" text-anchor="middle">FAMILY RESERVE</text>

    <g class="badge">
      <use href="#badge-shape" class="frame-outer"/>
      <use href="#badge-shape" class="frame-mid" transform="translate(405 524) scale(0.965) translate(-405 -524)"/>
      <use href="#badge-shape" class="frame-inner" transform="translate(405 524) scale(0.92) translate(-405 -524)"/>

      <ellipse class="tree-art" cx="405" cy="305" rx="80" ry="62" role="img" aria-label="Illustration of an olive tree"/>
      <line class="rule" x1="228" y1="383" x2="582" y2="383" stroke-width="2"/>

      <text class="brand-name" x="405" y="520" text-anchor="middle">Casa Lumbre</text>
      <line class="rule" x1="133" y1="548" x2="670" y2="548" stroke-width="4"/>
      <line class="rule" x1="163" y1="561" x2="640" y2="561" stroke-width="2"/>

      <text class="variety-name" x="405" y="665" text-anchor="middle">Picual</text>

      <ellipse class="branch-art" cx="420" cy="728" rx="90" ry="34" role="img" aria-label="Illustration of an olive branch with dark olives"/>
    </g>

    <text class="product-type" x="405" y="945" text-anchor="middle">Extra Virgin Olive Oil</text>
    <text class="volume" x="405" y="1045" text-anchor="middle">500 <tspan class="volume-unit">ML</tspan></text>
  </g>
</svg>
</body>
</html>
```